Corvale Motorized Shade Business Card

Hello, we've had our logo made. Now we are looking for a clean and cool looking business card. One side can just be the logo with any design elements that might look good with it. The other side will be Name, Phone Number and Email. There will not be an address on the card.

```html
<!DOCTYPE html>
<html lang="en">
<head>
<meta charset="UTF-8">
<title>Corvale Motorized Shade – Business Card</title>
<link href="https://fonts.googleapis.com/css2?family=Signika:wght@400;600;700&display=swap" rel="stylesheet">
<style>
  :root {
    --backdrop: #b3b3b3;
    --card-white: #ffffff;
    --card-yellow: #fec014;
    --brand-navy: #1f3f73;
    --brand-blue: #2a9fd8;
    --rule-grey: #9aa7b8;
    --text-white: #ffffff;
  }
  * { margin: 0; padding: 0; box-sizing: border-box; }
  html, body { width: 1200px; height: 800px; overflow: hidden; }
  body {
    background: var(--backdrop);
    font-family: "Signika", Arial, sans-serif;
    position: relative;
  }
  .card {
    position: absolute;
    top: 272px;
    width: 442px;
    height: 254px;
    box-shadow: 0 1px 2px rgba(0,0,0,0.12);
  }
  .card--front { left: 136px; background: var(--card-white); }
  .card--back  { left: 620px; background: var(--card-yellow); }

  .wordmark {
    position: absolute;
    display: flex;
    align-items: center;
    gap: 6px;
    color: var(--brand-navy);
    font-weight: 700;
    line-height: 1;
    text-transform: uppercase;
  }
  .wordmark__mark { background: var(--brand-blue); flex: none; }
  .card--front .wordmark { left: 36px; top: 72px; font-size: 24px; }
  .card--front .wordmark__mark { width: 16px; height: 16px; }
  .card--back .wordmark { left: 50%; top: 86px; transform: translateX(-50%); font-size: 52px; gap: 12px; }
  .card--back .wordmark__mark { width: 36px; height: 36px; }

  .divider {
    position: absolute;
    left: 36px; top: 133px;
    width: 370px; height: 1px;
    background: var(--rule-grey);
  }
  .holder {
    position: absolute;
    right: 36px; top: 110px;
    text-align: right;
  }
  .holder__name {
    color: var(--brand-blue);
    font-size: 19px;
    font-weight: 600;
    line-height: 20px;
  }
  .holder__title {
    margin-top: 8px;
    color: var(--brand-navy);
    font-size: 9px;
    font-weight: 700;
    letter-spacing: 1.6px;
  }
  .contact {
    position: absolute;
    left: 54px; top: 158px;
    list-style: none;
    color: var(--brand-blue);
    font-size: 10px;
    font-weight: 700;
    line-height: 18px;
  }
  .web {
    position: absolute;
    left: 0; right: 0; top: 228px;
    text-align: center;
    color: var(--text-white);
    font-size: 10px;
    font-weight: 700;
    letter-spacing: 2.4px;
    text-transform: uppercase;
  }
</style>
</head>
<body>
  <section class="card card--front">
    <div class="wordmark"><span class="wordmark__mark"></span><span>Corvale</span></div>
    <div class="holder">
      <div class="holder__name">Mara Ellison</div>
      <div class="holder__title">PRESIDENT</div>
    </div>
    <div class="divider"></div>
    <ul class="contact">
      <li>555.214.7730</li>
      <li>555.832.0419</li>
      <li>info@corvale.com</li>
      <li>www.corvale.com</li>
    </ul>
  </section>

  <section class="card card--back">
    <div class="wordmark"><span class="wordmark__mark"></span><span>Corvale</span></div>
    <div class="web">www.corvale.com</div>
  </section>
</body>
</html>
```